Real Estate Biz Card

-Card Size: Standard
-Background: Dark grey or black. I am open to gradient or a textured background.
-Other Colors: I dont mind pops of color. Contrasty blue, lime green, red Etc. Feel free to get creative.
-Text color: be creative
-Font: I like modern styles. Something that works well with my KV718 logo. See attached
-I would like my logo (KV718) watermarked on the card. Either on one side or both.
-Front of Card: keep it simple. Head shot, name, Logo, Phone #
-Back: add the rest of the details. See list below.
-brokerages logo as well as the Domivest and Equal Housing Opportunity logos on the card
-Name: Tod Marwick
-Residential Real Estate
-Cell:
-Email:
-Site:
-Office Address:
-very small/fine print "Each office independently owned & operated

```html
<!DOCTYPE html>
<html lang="en">
<head>
<meta charset="utf-8">
<title>KV718 Business Card</title>
<link rel="stylesheet" href="https://fonts.googleapis.com/css2?family=Exo+2:wght@600;700&family=Roboto:wght@400;500&display=swap">
<style>
:root{
  --page:#e9e7e4;
  --card-front:#f4f4f4;
  --card-back:#7f7f7f;
  --accent-red:#ee1c1c;
  --name-blue:#1a73c4;
  --text-grey:#808080;
  --white:#ffffff;
  --watermark:rgba(255,255,255,0.12);
  --photo-a:#c9ccd3;
  --photo-b:#4a6aa8;
}
*{margin:0;padding:0;box-sizing:border-box}
html,body{width:1200px;height:960px;overflow:hidden;background:var(--page)}
.canvas{position:relative;width:1200px;height:960px}
.card{position:absolute;width:600px;height:342px;overflow:hidden;box-shadow:0 3px 8px rgba(0,0,0,.25)}
.card-front{left:302px;top:129px;background:var(--card-front)}
.card-back{left:299px;top:489px;background:var(--card-back)}

.headshot{position:absolute;right:0;top:0;width:332px;height:342px;
  background:linear-gradient(180deg,var(--photo-a) 0%,#b7bdc8 30%,var(--photo-b) 70%,#3d5b98 100%);
  clip-path:polygon(20% 0,100% 0,100% 100%,0 100%,14% 60%)}

.brand-name{position:absolute;left:44px;top:150px;font-family:Roboto,sans-serif;font-weight:500;
  font-size:56px;line-height:1;color:var(--name-blue);letter-spacing:2px}
.brand-line{position:absolute;left:45px;top:210px;font-family:Roboto,sans-serif;font-weight:400;
  font-size:10px;letter-spacing:3.2px;color:var(--text-grey);text-transform:uppercase}

.accent-tab{position:absolute;left:0;top:240px;width:10px;height:64px;background:var(--accent-red);border-radius:0 8px 8px 0}
.agent{position:absolute;left:44px;top:244px;font-family:"Exo 2",sans-serif}
.agent-name{font-size:20px;font-weight:700;color:var(--name-blue);letter-spacing:.5px;line-height:24px}
.agent-role{font-size:14.5px;font-weight:600;color:var(--accent-red);line-height:18px}
.agent-phone{font-size:15px;font-weight:600;color:var(--text-grey);letter-spacing:1px;line-height:22px}

.contact{position:absolute;left:44px;top:40px;font-family:Roboto,sans-serif;color:var(--white)}
.address{font-size:14px;line-height:17px;margin-bottom:9px}
.contact-row{display:flex;align-items:center;font-size:14px;line-height:19.5px}
.contact-row svg{width:12px;height:12px;margin-right:10px;fill:var(--white)}
.fine-print{font-size:8px;margin-top:9px}

.affiliations{position:absolute;left:351px;top:43px;display:flex;align-items:center;gap:7px}
.badge{width:28px;height:30px;background:var(--white);border-radius:2px}
.brokerage{margin-left:4px;font-family:Roboto,sans-serif;color:var(--white)}
.brokerage-name{font-size:19px;font-weight:500;line-height:20px;letter-spacing:-.3px}
.brokerage-sub{font-size:9px;line-height:11px;letter-spacing:.3px}

.watermark{position:absolute;left:30px;top:205px;font-family:Roboto,sans-serif;font-weight:500;
  font-size:140px;line-height:1;color:var(--watermark);letter-spacing:6px}
</style>
</head>
<body>
<div class="canvas">
  <section class="card card-front">
    <div class="headshot" role="img" aria-label="Headshot of agent Tod Marwick in a blue shirt"></div>
    <div class="brand-name">KV718</div>
    <div class="brand-line">Homes for every chapter</div>
    <div class="accent-tab"></div>
    <div class="agent">
      <div class="agent-name">TOD MARWICK</div>
      <div class="agent-role">Residential Real Estate</div>
      <div class="agent-phone">555 210 4786</div>
    </div>
  </section>

  <section class="card card-back">
    <div class="watermark">KV718</div>
    <div class="contact">
      <div class="address">1420 Larkspur Way<br>Fairview, Oregon 97024</div>
      <div class="contact-row">
        <svg viewBox="0 0 24 24"><path d="M6.6 10.8a15.1 15.1 0 0 0 6.6 6.6l2.2-2.2a1 1 0 0 1 1-.25 11.4 11.4 0 0 0 3.6.57 1 1 0 0 1 1 1V20a1 1 0 0 1-1 1A17 17 0 0 1 3 4a1 1 0 0 1 1-1h3.5a1 1 0 0 1 1 1c0 1.25.2 2.45.57 3.570a1 1 0 0 1-.25 1z"/></svg>
        555 318 0942
      </div>
      <div class="contact-row">
        <svg viewBox="0 0 24 24"><path d="M2 5h20v14H2z M2 5l10 8 10-8" fill="none" stroke="#fff" stroke-width="2.4"/></svg>
        tod@kv718.com
      </div>
      <div class="contact-row">
        <svg viewBox="0 0 24 24"><circle cx="12" cy="12" r="10" fill="none" stroke="#fff" stroke-width="2.4"/><path d="M2 12h20M12 2c3 3 3 17 0 20M12 2c-3 3-3 17 0 20" fill="none" stroke="#fff" stroke-width="1.8"/></svg>
        www.kv718.com
      </div>
      <div class="fine-print">Each office independently owned &amp; operated</div>
    </div>
    <div class="affiliations">
      <div class="badge" role="img" aria-label="Domivest membership badge"></div>
      <div class="badge" role="img" aria-label="Equal housing opportunity badge"></div>
      <div class="brokerage">
        <div class="brokerage-name">HARBORVIEW</div>
        <div class="brokerage-sub">REALTY GROUP</div>
      </div>
    </div>
  </section>
</div>
</body>
</html>
```